Business Card Design Project

WE NEED A CARD WITH THE NAME AND LOGO IN ONE SIDE AND THE ODER JUST THE INFORMATIONS LIKE NAME, E-MAIL, PHONE AND SITE. I HAVE A IDEA OF THE CARD ALL BLACK AND JUST COLLOORS IN THE LOGO AND INFORMATIONS. WE WANT SANTHING SIMPLE AND ELEGANT. SAMETHING NEW WICTH PASS CONFIANCE.
Updates

I HAVE UP DATE THE INFORMATIONS OF WAHT WE NEED. THNKSĀ 

Target Market(s)

COMPANY WHO ORGANIZE BIG CORPORATIVE EVENTS.

Industry/Entity Type

Business

Requirements
Should not have
• MUCH INFORMATION.

```html
<!DOCTYPE html>
<html lang="en">
<head>
<meta charset="utf-8">
<title>Business Card</title>
<link rel="stylesheet" href="https://fonts.googleapis.com/css2?family=Aldrich&family=Oswald:wght@500&family=Michroma&display=swap">
<style>
  :root {
    --page: #ffffff;
    --edge: #1b1a16;
    --steel-dark: #2b2922;
    --steel-mid: #4d4a43;
    --steel-base: #56534c;
    --steel-light: #8f8c85;
    --steel-glint: #a19f98;
    --ink: #ffffff;
  }
  * { margin: 0; padding: 0; box-sizing: border-box; }
  html, body {
    width: 1200px;
    height: 664px;
    overflow: hidden;
    background: var(--page);
  }
  .card {
    position: relative;
    width: 1200px;
    height: 664px;
    border: 7px solid var(--edge);
    border-radius: 52px;
    overflow: hidden;
    background: linear-gradient(118deg,
      var(--steel-dark) 0%,
      var(--steel-light) 9%,
      var(--steel-base) 20%,
      var(--steel-mid) 40%,
      var(--steel-mid) 58%,
      var(--steel-base) 68%,
      var(--steel-glint) 78%,
      var(--steel-base) 88%,
      var(--steel-dark) 100%);
    color: var(--ink);
  }
  .identity {
    position: absolute;
    right: 452px;
    top: 112px;
    text-align: right;
  }
  .identity__name {
    font-family: "Michroma", sans-serif;
    font-size: 58px;
    line-height: 1;
    letter-spacing: 2px;
    color: var(--steel-base);
    -webkit-text-stroke: 2px var(--ink);
    transform: scaleX(1.12);
    transform-origin: right center;
  }
  .identity__role {
    margin-top: 6px;
    font-family: "Oswald", sans-serif;
    font-weight: 500;
    font-size: 50px;
    line-height: 1.1;
  }
  .divider {
    position: absolute;
    left: 779px;
    top: 90px;
    width: 6px;
    height: 225px;
    background: var(--ink);
  }
  .contact {
    position: absolute;
    left: 812px;
    display: flex;
    align-items: center;
    font-family: "Aldrich", sans-serif;
    font-size: 26px;
    letter-spacing: 1.5px;
  }
  .contact--phone { top: 92px; }
  .contact--mobile { top: 190px; }
  .contact--email { top: 284px; }
  .contact svg { flex: none; margin-right: 22px; }
  .organization {
    position: absolute;
    left: 86px;
    top: 414px;
    font-family: "Oswald", sans-serif;
    font-weight: 500;
    font-size: 54px;
    line-height: 1.1;
  }
  .address {
    position: absolute;
    left: 84px;
    top: 500px;
    display: flex;
    align-items: flex-start;
  }
  .address svg { flex: none; margin-right: 10px; margin-top: 2px; }
  .address__lines {
    font-family: "Aldrich", sans-serif;
    font-size: 26px;
    line-height: 33px;
    letter-spacing: 1.5px;
  }
</style>
</head>
<body>
  <div class="card">
    <div class="identity">
      <div class="identity__name">NAME</div>
      <div class="identity__role">Position</div>
    </div>

    <div class="divider"></div>

    <div class="contact contact--phone">
      <svg width="22" height="34" viewBox="0 0 22 34" aria-hidden="true">
        <path d="M6 1h8v9H9c-1 5-1 9 0 14h5v9H6C1 28 0 22 0 17S1 6 6 1z" fill="#ffffff"/>
      </svg>
      <span>1234567890</span>
    </div>

    <div class="contact contact--mobile">
      <svg width="28" height="30" viewBox="0 0 28 30" aria-hidden="true">
        <rect x="0" y="0" width="28" height="30" rx="3" fill="#111"/>
        <rect x="3" y="3" width="22" height="18" fill="#ffffff"/>
        <rect x="9" y="24" width="10" height="2" fill="#ffffff"/>
      </svg>
      <span>1234567890</span>
    </div>

    <div class="contact contact--email">
      <svg width="42" height="26" viewBox="0 0 42 26" aria-hidden="true">
        <path d="M0 0h42v26H0z" fill="#111"/>
        <path d="M2 2h38L21 14z" fill="#ffffff"/>
        <path d="M2 24l14-10 5 3 5-3 14 10z" fill="#ffffff"/>
        <circle cx="21" cy="7" r="3" fill="none" stroke="#111" stroke-width="1.2"/>
      </svg>
      <span>abc@xyz.com</span>
    </div>

    <div class="organization">Organization Name</div>

    <div class="address">
      <svg width="26" height="36" viewBox="0 0 26 36" aria-hidden="true">
        <path d="M13 1a9 9 0 0 0-9 9c0 7 9 16 9 16s9-9 9-16a9 9 0 0 0-9-9zm0 5a4 4 0 1 1 0 8 4 4 0 0 1 0-8z" fill="#ffffff"/>
        <path d="M0 35l6-7h14l6 7z" fill="#ffffff"/>
      </svg>
      <div class="address__lines">
        <div>Address line 1</div>
        <div>Address line 2</div>
        <div>Address line 3</div>
      </div>
    </div>
  </div>
</body>
</html>
```